Need somewhat upscale, eye catching honey jar label to make our product stand out on store shelves.

We need front and back labels for a honey jar. Files "Honey Jar Front Label 2" & "Honey Jar Back Label 2" show what I have come up with.

Files "Honey Jar Front Label 2". I did this as an example. It shows the information that needs to be included on the front label. The picture was taken by my daughter. The information and picture can be rearranged, enlarged, reduced, cropped, etc. as you see fit.

Files "Honey Jar Back Label 2". I did this one to play with the wording to get the information to fit. It explains how I keep bees. It can be worded differently as long as all the information is included.

I know nothing about good use of color, borders, backgrounds, font style and size, etc. so please excuse my plain presentations. I admire and respect your creative abilities very much.

Since my method of keeping bees involves a lot of travel time and expense, as mentioned in files "Honey Jar Back Label 2" I will try to price my honey a little higher than the competition so please design accordingly with that in mind.

We think we want to use a traditional jar with stick on labels like Tolvan's jar seen in file Tolvan's Jar. However, feel free to use a different jar as long as the honey can be easily scooped out with a spoon and does not have to be poured out. I know that eliminates a lot of fancy jars but that's what my customers want. Jar size should be 12 ounces which will hold a little more than 1 pound of honey.

Hanging labels are also acceptable therefore jar shapes that will not accept a stick on label can also be used. An example is a Honeypot Jar.

And of course we like Hexagon Jars which are 6 sided like the cells in honeycomb.

Please stick to glass jars that are readily available. No custom shaped jars for now.

Tolvan's jar is clear glass and the metal lid is a light golden color.

It's probably a good idea for the shape of the labels to match the shape of the bottle like I marked in black on Tolvan's Jar. Being wider in the middle should allow the back label to be shorter than my example seen in files "Honey Jar Back Label 2". I think front and back labels should be the same size.

The shape of the area marked in black around Tolvann's label measures 1-1/4 (1.25) inches across the top, 2-1/4 (2.25) inches across the middle, 2 inches across the bottom and 3-1/2 (3.5) inches tall from top to bottom.

Target Market(s)

People wanting local honey that is not processed in any way.
People that are willing to pay a little more for honey from bees that are kept in a sustainable way (see the story in files 2 & 17) without the use of harsh chemicals.

Industry/Entity Type

Travel

Font styles to use
Serif
Decorative
Script

Requirements
Must have
• See my lengthy project description, file "Honey Jar Front Label 2" and file "Honey Jar Back Label 2". All of the info. therein is very important.
• Somewhat upscale, eye catching appearance that makes the product stand out on store shelves and suggests that the honey inside is quality, unprocessed truly local honey.
Nice to have
• If bullets are used they can look like a skep (type of beehive). I have included an example in a file.
• Swirly dashed line coming off the s in lor-Wren's with a honeybee at the end of it. See files for examples.
• Swirly dashed line coming off the i in wildflower making the shape of a heart with a honeybee at the end of it hovering over the o in wildflower and the o looks like a flower. See files for examples.

```html
<!DOCTYPE html>
<html lang="en">
<head>
<meta charset="utf-8">
<title>Local Honey – Jar Labels</title>
<link rel="stylesheet" href="https://fonts.googleapis.com/css2?family=Arimo:wght@400;700&family=Lobster&family=Encode+Sans+Condensed:wght@400;600;700&family=Open+Sans:ital,wght@1,400&display=swap">
<style>
  :root {
    --paper: #ffffff;
    --rim-dark: #7a4a1c;
    --rim-mid: #b57a3a;
    --rim-light: #f1d3a0;
    --gold-deep: #d99a1c;
    --gold: #efb53a;
    --gold-pale: #f3d79a;
    --ink: #1a1206;
    --photo-pink: #e25a9a;
    --photo-green: #3f5a2a;
  }
  * { margin: 0; padding: 0; box-sizing: border-box; }
  html, body { width: 1200px; height: 757px; overflow: hidden; background: var(--paper); }
  .canvas { position: relative; width: 1200px; height: 757px; }
  .label-shape { position: absolute; top: 0; left: 0; }
  .label-text { position: absolute; color: var(--ink); text-align: center; }

  .brand { font-family: "Arimo", sans-serif; font-weight: 700; font-size: 30px; letter-spacing: 3px; text-transform: uppercase; }
  .script { font-family: "Lobster", cursive; }
  .claims { font-family: "Arimo", sans-serif; font-weight: 700; font-size: 17px; line-height: 21px; letter-spacing: 0.3px; }

  .front { left: 200px; width: 340px; }
  .front-brand { top: 144px; }
  .front-title { top: 194px; font-size: 48px; }
  .front-claims { top: 254px; }
  .photo-caption { top: 463px; left: 318px; width: 116px; font-size: 14px; line-height: 15px; color: #2a1a08; }
  .variety { top: 516px; font-family: "Arimo", sans-serif; font-weight: 700; font-size: 32px; letter-spacing: 0.5px; }
  .weight { top: 566px; }

  .back { left: 620px; width: 340px; }
  .back-city { top: 100px; font-family: "Arimo", sans-serif; font-weight: 700; font-size: 20px; }
  .back-title { top: 122px; font-size: 36px; }
  .counties { top: 170px; left: 660px; width: 260px; font-family: "Open Sans", sans-serif; font-style: italic; font-size: 10.5px; line-height: 13px; }
  .story { font-family: "Encode Sans Condensed", sans-serif; font-size: 12px; line-height: 13.5px; }
  .story-main { top: 220px; left: 650px; width: 280px; }
  .story-pledge { top: 340px; left: 675px; width: 250px; }
  .story-only { top: 380px; left: 675px; width: 250px; }
  .skep { display: inline-block; width: 16px; height: 12px; border-radius: 50% 50% 20% 20%; background: var(--ink); vertical-align: -1px; margin-right: 6px; }
  .warning { top: 414px; font-family: "Encode Sans Condensed", sans-serif; font-weight: 700; font-size: 11px; }
  .nutrition { font-family: "Encode Sans Condensed", sans-serif; font-size: 10px; line-height: 11.5px; }
  .nutrition-left { top: 442px; left: 680px; width: 115px; }
  .nutrition-left b { font-weight: 700; }
  .nutrition-right { top: 438px; left: 800px; width: 105px; }
  .back-brand { top: 560px; }
  .url { top: 612px; font-family: "Arimo", sans-serif; font-weight: 700; font-size: 13px; }
</style>
</head>
<body>
<main class="canvas">
  <svg class="label-shape" width="1200" height="757" viewBox="0 0 1200 757" aria-hidden="true">
    <defs>
      <linearGradient id="rim" x1="0" y1="0" x2="1" y2="0">
        <stop offset="0" stop-color="var(--rim-dark)"/>
        <stop offset="0.12" stop-color="var(--rim-light)"/>
        <stop offset="0.5" stop-color="var(--rim-mid)"/>
        <stop offset="0.88" stop-color="var(--rim-light)"/>
        <stop offset="1" stop-color="var(--rim-dark)"/>
      </linearGradient>
      <radialGradient id="front-field" cx="0.5" cy="0.45" r="0.6">
        <stop offset="0" stop-color="var(--gold)"/>
        <stop offset="1" stop-color="var(--gold-deep)"/>
      </radialGradient>
      <radialGradient id="back-field" cx="0.5" cy="0.45" r="0.6">
        <stop offset="0" stop-color="var(--gold-pale)"/>
        <stop offset="1" stop-color="#d9a455"/>
      </radialGradient>
      <linearGradient id="photo" x1="0" y1="0" x2="0" y2="1">
        <stop offset="0" stop-color="var(--photo-green)"/>
        <stop offset="0.45" stop-color="#a05a5a"/>
        <stop offset="1" stop-color="var(--photo-pink)"/>
      </linearGradient>
    </defs>
    <g class="front-label">
      <ellipse cx="370" cy="373" rx="170" ry="342" fill="url(#rim)"/>
      <ellipse cx="370" cy="373" rx="155" ry="327" fill="url(#front-field)"/>
      <polygon points="315,318 430,318 482,413 430,510 315,510 263,413" fill="#c9962e"/>
      <polygon points="320,326 425,326 472,413 425,502 320,502 273,413" fill="url(#photo)" role="img" aria-label="Photograph of a honeybee on a pink hibiscus flower"/>
    </g>
    <g class="back-label">
      <ellipse cx="790" cy="373" rx="170" ry="342" fill="url(#rim)"/>
      <ellipse cx="790" cy="373" rx="155" ry="327" fill="url(#back-field)"/>
    </g>
  </svg>

  <!-- Front label -->
  <div class="label-text front front-brand brand">lor-Wren's</div>
  <div class="label-text front front-title script">Local Honey</div>
  <div class="label-text front front-claims claims">100% Pure, Raw, Unaltered<br>Never Heated<br>Strained Not Micro-Filtered</div>
  <div class="label-text photo-caption script">She Works Hard<br>For The Honey</div>
  <div class="label-text front variety">WILDFLOWER</div>
  <div class="label-text front weight claims">Net Weight 16 oz/454g<br>(24 liquid oz)</div>

  <!-- Back label -->
  <div class="label-text back back-city">Atlanta's</div>
  <div class="label-text back back-title script">Local Honey</div>
  <div class="label-text counties">Bees kept in Cobb, Cherokee, DeKalb, Douglas, Forsyth, Gwinnett, Hall &amp; Jackson Counties.<br>Sustainable Beekeeping</div>
  <p class="label-text story story-main"><span class="skep"></span>Partnering with local farmers and landowners we spread our bees out over many square miles, keeping fewer bees at more locations. Although much more time consuming and expensive, it allows the pollinators to benefit more of the environment and ensures them more abundant natural food. This eliminates the need to feed cane sugar or high fructose corn syrups which results in healthier bees and purer honey, not contaminated with syrup.</p>
  <p class="label-text story story-pledge"><span class="skep"></span>We will never sacrifice the health of the bees or the quality of their honey for profit. Never!</p>
  <p class="label-text story story-only"><span class="skep"></span>We sell honey from our bees only.</p>
  <div class="label-text back warning">Do not feed to infants under 1 year old.</div>
  <div class="label-text nutrition nutrition-left"><b>Nutrition Facts</b><br>Serv. Size 1 Tbsp (21g)<br>Serv. Per Container 21<br>Percent Daily Values (DV) are based on a 2,000 calorie diet.</div>
  <div class="label-text nutrition nutrition-right">Amount Per Serving<br>Calories 64<br>Total Fat 0g 0% DV<br>Sodium 0mg 0% DV<br>Total Carbs 17g 6% DV<br>Sugars 16g<br>Protein 0g 0% DV</div>
  <div class="label-text back back-brand brand">lor-Wren's</div>
  <div class="label-text back url">www.lorwrenhoney.com</div>
</main>
</body>
</html>
```